Marquise Velvet Stable Goods - Elite line of horse care grooming products

I wanted to have a label design for my equestrian products that made the people who use them on their horses feel like a princess. I use all natural ingredients, they smell wonderful and work! I think my current design could be more amazing.... I have a total of 6 products. The final design should communicate that you are using the finest and highest quality ingredients on your best friend. please see my website (www.MarquiseStable.example) for the design aesthetic I'm going for. Design Guide:
The design should communicate that you are using the finest and highest quality ingredients on your best friend.
Create a bold, unique, visually-appealing design
Make buyer feel like a princess
Impart that you are taking care of your horse because you’re buying the best
Stand out from most other products currently on the market that look boring/outdated, bland
Avoid any design or visual images that impart chemical, industrial or commercial connotations
Key Terms: Elite, Bold, Serious, Baroque elegance, Feminine, Elegance, Wow, Fairytale, Fantasy, Elegance,

Please create: Design separate front and back BOPP labels for 32oz. spray bottle, 3.5x5” Rosemary, Lavender & Mint Insect Repellent

Design should convey a sense of wealth and prestige
Elegance & sophistication
Professional quality

Design Guide:

Key Attributes of Product:
Expensive product
Therapeutic-grade essential oils
All-natural ingredients
No poisons or pesticides
Smell wonderful
They work

Please use royal purple and gold

Target Market(s)

High end female horse owners..12-65yo female horse owners who want to and can afford to buy premium products for horse grooming.

Font styles to use
Sans Serif
Decorative
Script

Colors
876aae

Requirements
Must have
• Elegance, wow, pick me. Mandatory Graphics:
• Marquise Velvet Stable Goods logo with gold doily (no gradient on gold)
Nice to have
• Fairytale, fantasy, quality, elite, smells good,
Should not have
• I do not want my bottles to look like pesticides or poison.

```html
<!DOCTYPE html>
<html lang="en">
<head>
<meta charset="utf-8">
<title>Marquise Velvet Stable Goods – Natural Insect Repellent Label</title>
<link rel="stylesheet" href="https://fonts.googleapis.com/css2?family=Marcellus&family=Open+Sans:wght@400;600&family=Pinyon+Script&display=swap">
<style>
  :root {
    --royal-purple: #6e2384;
    --deep-purple: #5a1a6e;
    --band-purple: #74268a;
    --gold-light: #e9c983;
    --gold-mid: #c9a05a;
    --gold-dark: #a9813f;
    --ink: #1d1d1d;
    --paper: #ffffff;
  }
  html, body {
    margin: 0;
    padding: 0;
    width: 976px;
    height: 1200px;
    overflow: hidden;
    background: var(--paper);
  }
  .canvas {
    position: relative;
    width: 976px;
    height: 1200px;
  }
  .label-art {
    position: absolute;
    inset: 0;
  }
  .brand-doily {
    position: absolute;
    left: 356px;
    top: 186px;
    width: 264px;
    height: 290px;
    border-radius: 50%;
    background: radial-gradient(circle, var(--gold-light) 0%, var(--gold-mid) 60%, var(--gold-dark) 100%);
    opacity: 0.85;
  }
  .brand-seal {
    position: absolute;
    left: 384px;
    top: 227px;
    width: 208px;
    height: 208px;
    border-radius: 50%;
    background: var(--paper);
    box-shadow: 0 0 0 3px var(--gold-light);
    display: flex;
    align-items: center;
    justify-content: center;
  }
  .brand-name {
    margin: 0;
    width: 170px;
    text-align: center;
    font-family: "Open Sans", sans-serif;
    font-weight: 600;
    font-size: 21px;
    line-height: 1.2;
    color: var(--royal-purple);
  }
  .product-title {
    position: absolute;
    left: 0;
    width: 976px;
    top: 484px;
    margin: 0;
    text-align: center;
    font-family: "Marcellus", serif;
    font-weight: 400;
    font-size: 50px;
    letter-spacing: 0.6px;
    white-space: nowrap;
    color: var(--royal-purple);
  }
  .scent-blend {
    position: absolute;
    left: 0;
    width: 976px;
    top: 594px;
    margin: 0;
    text-align: center;
    font-family: "Open Sans", sans-serif;
    font-size: 22px;
    letter-spacing: 2.5px;
    white-space: nowrap;
    color: var(--ink);
  }
  .benefits {
    position: absolute;
    left: 158px;
    width: 660px;
    top: 692px;
    margin: 0;
    text-align: center;
    font-family: "Open Sans", sans-serif;
    font-size: 27px;
    line-height: 39px;
    white-space: nowrap;
    color: var(--paper);
  }
  .tagline {
    position: absolute;
    left: 0;
    width: 976px;
    top: 904px;
    margin: 0;
    text-align: center;
    font-family: "Pinyon Script", cursive;
    font-size: 48px;
    color: var(--ink);
  }
  .flourish {
    position: absolute;
    left: 458px;
    top: 976px;
  }
</style>
</head>
<body>
<main class="canvas">
  <svg class="label-art" width="976" height="1200" viewBox="0 0 976 1200" aria-hidden="true">
    <defs>
      <linearGradient id="gold-band" x1="0" y1="0" x2="1" y2="1">
        <stop offset="0" stop-color="#b58a45"/>
        <stop offset="0.35" stop-color="#f0d494"/>
        <stop offset="0.6" stop-color="#c39a55"/>
        <stop offset="1" stop-color="#e6c681"/>
      </linearGradient>
      <linearGradient id="velvet" x1="0" y1="0" x2="0" y2="1">
        <stop offset="0" stop-color="#6a1f80"/>
        <stop offset="1" stop-color="#5e1a73"/>
      </linearGradient>
    </defs>
    <rect class="label-body" x="116" y="67" width="744" height="1063" rx="26" fill="url(#velvet)"/>
    <path class="frame-edge" fill="#ffffff"
      d="M158,340 C200,200 330,103 488,103 C646,103 776,200 818,340 L818,900 C818,1010 660,1088 488,1088 C316,1088 158,1010 158,900 Z"/>
    <path class="frame-gold" fill="url(#gold-band)"
      d="M171,345 C212,212 338,116 488,116 C638,116 764,212 805,345 L805,895 C805,1000 652,1075 488,1075 C324,1075 171,1000 171,895 Z"/>
    <path class="frame-panel" fill="#ffffff"
      d="M201,355 C240,235 352,150 488,150 C624,150 736,235 775,355 L775,885 C775,980 640,1045 488,1045 C336,1045 201,980 201,885 Z"/>
    <line class="divider" x1="205" y1="569" x2="468" y2="569" stroke="#6e2384" stroke-width="2.5"/>
    <line class="divider" x1="508" y1="569" x2="749" y2="569" stroke="#6e2384" stroke-width="2.5"/>
    <rect class="divider-gem" x="480" y="561" width="16" height="16" fill="#6e2384" transform="rotate(45 488 569)"/>
    <path class="banner-edge" fill="#ffffff"
      d="M138,652 Q488,634 838,652 L830,900 Q488,880 144,904 Z"/>
    <path class="banner" fill="#74268a"
      d="M146,660 Q488,642 830,660 L823,892 Q488,872 151,896 Z"/>
  </svg>

  <div class="brand-doily" role="img" aria-label="Gold baroque doily ornament framing the brand seal"></div>
  <div class="brand-seal">
    <p class="brand-name">Marquise Velvet Stable Goods</p>
  </div>

  <h1 class="product-title">Natural Insect Repellent</h1>
  <p class="scent-blend">LAVENDER, MINT &amp; ROSEMARY BLEND</p>

  <p class="benefits">Natural ingredients made with therapeutic<br>grade essential oils! Free of harsh chemicals,<br>lovely smell. Safe for humans too...go ahead,<br>spray it on yourself!</p>

  <p class="tagline">Love your horse!</p>
  <svg class="flourish" width="60" height="18" viewBox="0 0 60 18" role="img" aria-label="Small purple flourish ornament">
    <ellipse cx="30" cy="10" rx="26" ry="5" fill="#74268a" opacity="0.8"/>
  </svg>
</main>
</body>
</html>
```